Business Card Design

we are a brand new cable TV network devoted to self improvement and leading a better life called FLOURIVO TV.I have a logo. We have 3 executives that need cards.I want it to be a heavy stock card: professional but showing our creative nature

Industry/Entity Type

Business

Contact Information for Business Card

CLAUDIA SAENZ AMLIECEO350 San Juan DrPonte Vedra Beach FL 32082904-473-5953

```html
<!DOCTYPE html>
<html lang="en">
<head>
<meta charset="utf-8">
<title>FLOURIVO TV – Business Card</title>
<link href="https://fonts.googleapis.com/css2?family=Roboto+Condensed:wght@300;400;700&display=swap" rel="stylesheet">
<style>
  :root {
    --page-bg: #d9dcdc;
    --card-white: #ffffff;
    --ink: #1e1e1e;
    --plum: #8a2a6c;
    --magenta: #c42477;
    --pink: #e2307f;
    --on-panel: #ffffff;
    --icon-bg: #ffffff;
    --icon-ink: #8a2a6c;
  }
  * { margin: 0; padding: 0; box-sizing: border-box; }
  html, body {
    width: 1200px; height: 1000px; overflow: hidden;
    background: var(--page-bg);
    font-family: "Roboto Condensed", "Arial Narrow", sans-serif;
  }
  .card {
    position: absolute; left: 340px; top: 90px;
    width: 520px; height: 820px;
    background: var(--card-white);
    box-shadow: 0 6px 18px rgba(0,0,0,.18);
  }
  .card__panel { position: absolute; inset: 0; }
  .brand {
    position: absolute; left: 30px; top: 140px;
    font-size: 56px; font-weight: 700; letter-spacing: -1px;
    color: var(--ink); line-height: 1;
  }
  .person {
    position: absolute; left: 52px; top: 262px;
    display: inline-block; color: var(--on-panel);
  }
  .person__name { font-size: 27px; font-weight: 300; letter-spacing: 1px; line-height: 1.1; }
  .person__title { font-size: 15px; font-weight: 300; letter-spacing: 1px; text-align: right; line-height: 1.2; }
  .divider {
    position: absolute; left: 52px; top: 470px;
    width: 300px; height: 2px; background: var(--on-panel);
  }
  .contact { position: absolute; left: 52px; color: var(--on-panel); font-size: 20px; font-weight: 400; line-height: 1.25; }
  .contact--address { top: 530px; }
  .contact--phone { top: 612px; }
  .contact__row { display: flex; align-items: center; gap: 18px; }
  .contact__icon { width: 34px; height: 34px; flex: none; }
</style>
</head>
<body>
  <div class="card">
    <svg class="card__panel" width="520" height="820" viewBox="0 0 520 820" role="img" aria-label="Magenta panel with a faint translucent triangle pattern">
      <defs>
        <linearGradient id="panelGradient" x1="0" y1="0" x2="1" y2="1">
          <stop offset="0" stop-color="var(--plum)"/>
          <stop offset="0.55" stop-color="var(--magenta)"/>
          <stop offset="1" stop-color="var(--pink)"/>
        </linearGradient>
      </defs>
      <polygon points="22,222 345,222 405,22 498,22 498,798 22,798" fill="url(#panelGradient)"/>
    </svg>

    <div class="brand">FLOURIVO TV</div>

    <div class="person">
      <div class="person__name">MIRELLA OKAFOR DUNST</div>
      <div class="person__title">CEO</div>
    </div>

    <div class="divider"></div>

    <div class="contact contact--address contact__row">
      <svg class="contact__icon" viewBox="0 0 34 34" aria-hidden="true">
        <circle cx="17" cy="17" r="17" fill="var(--icon-bg)"/>
        <rect x="9" y="11" width="16" height="12" fill="none" stroke="var(--icon-ink)" stroke-width="1.6"/>
        <polyline points="9,11 17,18 25,11" fill="none" stroke="var(--icon-ink)" stroke-width="1.6"/>
      </svg>
      <div>718 Harlow Creek Dr<br>Ponte Vedra Beach FL 32097</div>
    </div>

    <div class="contact contact--phone contact__row">
      <svg class="contact__icon" viewBox="0 0 34 34" aria-hidden="true">
        <circle cx="17" cy="17" r="17" fill="var(--icon-bg)"/>
        <path d="M12 10 l3 0 l1.5 4 l-2 1.5 q1.5 3 4 4.5 l1.5-2 l4 1.5 l0 3 q-1 1.5-3 1.5 q-9-1-10.5-11 q0-2 1.5-3z" fill="var(--icon-ink)"/>
      </svg>
      <div>904-618-2047</div>
    </div>
  </div>
</body>
</html>
```